BriskLoom Wordpress Website

We require a WordPress website that emulates the sleek design and functionality of https://www.tulvorix.example and https://quenlap.example/. The site should showcase our AI-powered customer support solutions with a modern, professional aesthetic.
Homepage
The homepage should feature a bold headline highlighting our AI capabilities, followed by concise sections outlining our key offerings:
AI-powered customer support
Data integration and deployment
Knowledge system integration
AI help desks and chat agents
Customer feedback insights
Include eye-catching visuals or animations to illustrate these concepts.
Navigation
The main navigation menu should include:
Product
Platform
Company
News
Learn More
Key Pages
Product Page: Detail our AI solutions, their benefits, and use cases.
Platform Page: Explain our technology, integration capabilities, and deployment process.
Company Page: Share our mission, team, and values.
News Page: Feature latest updates, press releases, and blog posts.
Call-to-Action
Implement a prominent "Learn More" button that directs users to an enrollment page. Our team will manage inquiries from this point.
Footer
Include a "Contact Us" section in the footer for easy access to our contact information.
Design Elements
Use a clean, minimalist design with ample white space
Incorporate a color scheme that reflects trust and innovation
Utilize smooth scrolling and subtle animations for enhanced user experience
Ensure mobile responsiveness for all devices
Technical Requirements
Build on WordPress for easy content management
Optimize for fast loading speeds and SEO
The website should convey our expertise in AI-driven customer support solutions while providing an intuitive user experience that guides visitors toward learning more about our services
Industry/Entity Type
AI Chat Agents

```html
<!DOCTYPE html>
<html lang="en">
<head>
<meta charset="utf-8">
<title>BriskLoom – AI Chat Agents</title>
<link href="https://fonts.googleapis.com/css2?family=Poppins:wght@400;500;600;700;800&display=swap" rel="stylesheet">
<style>
:root{
  --bg-top:#2f6c72;
  --bg-bottom:#2b5d61;
  --card:#4a9194;
  --card-deep:#3e8185;
  --accent:#5aa5a8;
  --ink:#2e6a70;
  --pale:#e3f2f2;
  --text:#ffffff;
  --muted:#d6ecec;
  --line:rgba(255,255,255,.18);
}
*{margin:0;padding:0;box-sizing:border-box}
html,body{width:1200px;height:3125px;overflow:hidden}
body{
  position:relative;
  font-family:"Poppins",sans-serif;color:var(--text);
  background:linear-gradient(180deg,var(--bg-top) 0%,#2d6569 45%,var(--bg-bottom) 100%);
}
.abs{position:absolute}
.brand{display:flex;align-items:center;gap:10px;font-weight:500;color:var(--text)}
.brand-dot{width:40px;height:40px;border-radius:50%;background:var(--text)}
.site-nav{left:121px;top:14px;width:956px;height:56px;display:flex;align-items:center;justify-content:space-between}
.site-nav .brand{font-size:28px}
.nav-links{display:flex;align-items:center;gap:38px;font-size:12px;font-weight:500}
.btn-outline{border:1.5px solid rgba(255,255,255,.6);border-radius:20px;padding:8px 20px;font-size:12px;font-weight:500}
.swoosh{position:relative;display:inline-block}
.swoosh::after{content:"";position:absolute;left:-4%;right:-2%;bottom:-6px;height:10px;border-bottom:3px solid var(--accent);border-radius:0 0 50% 50%/0 0 100% 100%}
.hero-title{left:182px;top:102px;font-size:58px;font-weight:700;line-height:1.1}
.hero-lead{left:184px;top:185px;font-size:12px;line-height:18px;color:var(--muted)}
.hero-cta{left:740px;top:186px;display:flex;align-items:center;gap:12px;font-size:12px;font-weight:600}
.badge{width:36px;height:36px;border-radius:50%;background:rgba(255,255,255,.18);border:1.5px solid rgba(255,255,255,.5);display:flex;align-items:center;justify-content:center}
.btn-pill{display:inline-flex;align-items:center;gap:10px;background:#fff;color:var(--ink);border-radius:22px;padding:6px 6px 6px 16px;font-size:11px;font-weight:500}
.btn-pill i{width:24px;height:24px;border-radius:50%;background:var(--ink);display:block}
.hero-media{left:121px;top:258px;width:956px;height:483px;border-radius:44px;
  background:radial-gradient(ellipse at 22% 35%,#74c6c6 0%,#3f9095 30%,#2a5d62 60%,#3a3530 100%)}
.section-title{left:0;width:1200px;text-align:center;font-size:34px;font-weight:700}
.feature{top:887px;height:239px;background:var(--card);border-radius:6px;padding:26px;overflow:hidden}
.feature .icon{width:76px;height:76px;margin-top:18px}
.feature h3{font-size:19px;font-weight:600;margin-top:32px}
.feature p{font-size:13px;line-height:19px;color:var(--muted);margin-top:6px}
.portrait-ring{left:186px;top:1290px;width:342px;height:352px;border-radius:50%;background:var(--card)}
.portrait{left:190px;top:1254px;width:322px;height:356px;border-radius:50%;border:5px solid #fff;
  background:radial-gradient(circle at 55% 40%,#dfe6e8 0%,#9fb0b4 45%,#4a5a5e 100%)}
.points{left:616px;top:1280px;width:470px}
.point{display:flex;gap:12px;padding:10px 14px;border-radius:8px;margin-bottom:14px}
.point.active{background:var(--card)}
.tick{flex:0 0 16px;height:16px;border-radius:50%;background:var(--accent);margin-top:4px;display:flex;align-items:center;justify-content:center}
.point.active .tick{background:#fff}
.point h4{font-size:15px;font-weight:500;line-height:19px}
.point p{font-size:11px;line-height:17.5px;color:var(--muted);margin-top:4px;white-space:nowrap}
.contact-box{left:203px;top:1704px;width:794px;height:183px;background:var(--card);border-radius:6px;text-align:center}
.contact-box h2{font-size:34px;font-weight:700;margin-top:34px}
.contact-box .btn-pill{margin-top:18px}
.hub{left:498px;top:2015px;width:204px;height:204px;border-radius:50%;background:#fff;display:flex;align-items:center;justify-content:center;color:var(--ink);font-size:26px;font-weight:600}
.offer{display:flex;align-items:center;gap:10px;font-size:15px;font-weight:500;line-height:19px}
.ico{width:56px;height:56px;border-radius:50%;background:var(--pale);border:5px solid var(--card);display:flex;align-items:center;justify-content:center;flex:0 0 56px}
.offer.left{text-align:right}
.ghost{left:0;width:1200px;top:2350px;text-align:center;font-size:94px;font-weight:800;color:rgba(255,255,255,.04);letter-spacing:1px}
.news{top:2553px;width:305px}
.news .thumb{height:173px;border-radius:6px}
.news .meta{font-size:9px;color:var(--accent);margin:12px 0 4px 12px}
.news .row{display:flex;justify-content:space-between;align-items:center;padding:0 0 0 12px}
.news h5{font-size:14px;font-weight:600;line-height:17px}
.arrow{width:20px;height:20px;border-radius:50%;background:var(--card);display:flex;align-items:center;justify-content:center}
.view-all{left:532px;top:2815px;width:135px;height:36px;border:1.5px solid rgba(255,255,255,.6);border-radius:20px;text-align:center;line-height:33px;font-size:11px;font-weight:600}
.foot-line{left:121px;width:956px;height:1px;background:var(--line)}
.vline{top:2903px;height:182px;width:1px;background:var(--line)}
.foot-col h6{font-size:14px;font-weight:600;margin-bottom:16px}
.foot-col li{list-style:none;font-size:9px;line-height:17.5px}
.contact-row,.social-row{display:flex;align-items:center;gap:10px;font-size:9px;margin-bottom:12px}
.contact-row i,.social-row i{width:22px;height:22px;border-radius:50%;background:var(--card);display:flex;align-items:center;justify-content:center}
.copy{left:0;width:1200px;top:3095px;text-align:center;font-size:8px;color:var(--muted)}
</style>
</head>
<body>

<header class="abs site-nav">
  <div class="brand"><span class="brand-dot"></span>BriskLoom</div>
  <nav class="nav-links">
    <span>Product</span><span>Platform</span><span>Company</span><span>News</span>
    <span class="btn-outline">Learn More</span>
  </nav>
</header>

<h1 class="abs hero-title">Meet <span class="swoosh">BriskLoom</span></h1>
<p class="abs hero-lead">Elevate your users' experience, a new type of conversation awaits.<br>Enhance your customer experience with BriskLoom's AI Assistant.</p>
<div class="abs hero-cta">Always ready, always on -
  <span class="badge"><svg width="20" height="20" viewBox="0 0 20 20" fill="none" stroke="#fff" stroke-width="1.5"><circle cx="10" cy="10" r="7"/><path d="M10 6v4l3 2"/></svg></span>
  <span class="btn-pill">GET STARTED <i></i></span></div>

<div class="abs hero-media" role="img" aria-label="Photo of a support agent at a computer surrounded by holographic AI figures"></div>

<h2 class="abs section-title" style="top:808px">Revolutionize your <span class="swoosh">Customer</span> Interactions:</h2>

<article class="abs feature" style="left:121px;width:305px">
  <svg class="icon" viewBox="0 0 76 76" role="img" aria-label="Question and answer icon"><circle cx="40" cy="36" r="32" fill="var(--ink)"/><circle cx="40" cy="36" r="25" fill="var(--pale)"/><path d="M12 66l8-14 8 8z" fill="var(--ink)"/><text x="40" y="43" text-anchor="middle" font-family="Poppins,sans-serif" font-size="20" font-weight="600" fill="var(--ink)">Q/A</text></svg>
  <h3>Get Answers</h3><p>Users will find the information<br>they need in seconds.</p></article>
<article class="abs feature" style="left:450px;width:300px">
  <svg class="icon" viewBox="0 0 76 76" role="img" aria-label="Light bulb icon"><circle cx="38" cy="30" r="24" fill="var(--pale)"/><path d="M28 50h20v8H28z" fill="var(--pale)"/><rect x="30" y="61" width="16" height="5" rx="2" fill="var(--pale)"/><path d="M38 14v16M30 30h16" stroke="var(--ink)" stroke-width="4"/></svg>
  <h3>Solve Problems</h3><p>Concerns will be Addressed<br>quickly with expert assistance</p></article>
<article class="abs feature" style="left:776px;width:301px">
  <svg class="icon" viewBox="0 0 76 76" role="img" aria-label="Target with cursor icon"><circle cx="34" cy="34" r="30" fill="var(--pale)"/><circle cx="34" cy="34" r="20" fill="var(--ink)"/><circle cx="34" cy="34" r="10" fill="var(--pale)"/><path d="M40 40l26 10-10 4-4 10z" fill="var(--pale)" stroke="var(--ink)" stroke-width="2"/></svg>
  <h3>Take Action</h3><p>Users will activate services<br>and features immediately</p></article>

<h2 class="abs section-title" style="top:1186px">All through Natural, Conversational <span class="swoosh">Experiences.</span></h2>

<div class="abs portrait-ring"></div>
<div class="abs portrait" role="img" aria-label="Illustration of a humanoid robot head in profile"></div>

<div class="abs points">
  <div class="point"><span class="tick"><svg width="9" height="9" viewBox="0 0 10 10"><path d="M2 5l2 2 4-4" stroke="#2e6a70" stroke-width="1.8" fill="none"/></svg></span><div><h4>BriskLoom Enables you to:</h4><p>Engage and delight customers with an AI agent aligned to your brand<br>Provide real-time support for a wide variety of uses from simple to complex</p></div></div>
  <div class="point active"><span class="tick"><svg width="9" height="9" viewBox="0 0 10 10"><path d="M2 5l2 2 4-4" stroke="#4a9194" stroke-width="1.8" fill="none"/></svg></span><div><h4>Make AI your own with BriskLoom's<br>Conversational Platform:</h4><p>Ground your BriskLoom AI agent in your company's identity &amp; knowledge<br>Solve problems quickly and effectively</p></div></div>
  <div class="point"><span class="tick"><svg width="9" height="9" viewBox="0 0 10 10"><path d="M2 5l2 2 4-4" stroke="#2e6a70" stroke-width="1.8" fill="none"/></svg></span><div><h4>BriskLoom prioritizes trust and security:</h4><p>Built-in supervision and auditing<br>Secure integrations<br>Strong data governance and privacy<br>Discover how BriskLoom can transform your customer<br>experience with customized<br>conversational AI.</p></div></div>
</div>

<section class="abs contact-box">
  <h2><span class="swoosh">Contact us</span> today</h2>
  <span class="btn-pill">LEARN MORE <i></i></span>
</section>

<h2 class="abs section-title" style="top:1938px">Our key <span class="swoosh">Offerings:</span></h2>

<svg class="abs" style="left:0;top:1980px" width="1200" height="380" aria-hidden="true">
  <g stroke="rgba(255,255,255,.25)" stroke-width="1" fill="none">
    <line x1="420" y1="78" x2="500" y2="78"/><line x1="700" y1="78" x2="775" y2="78"/>
    <line x1="448" y1="217" x2="500" y2="217"/><line x1="700" y1="217" x2="752" y2="217"/>
    <line x1="600" y1="240" x2="600" y2="292"/>
  </g>
  <g fill="rgba(255,255,255,.4)"><circle cx="496" cy="78" r="3"/><circle cx="700" cy="78" r="3"/><circle cx="500" cy="217" r="3"/><circle cx="700" cy="217" r="3"/><circle cx="600" cy="266" r="3"/></g>
</svg>
<div class="abs hub">BriskLoom</div>

<div class="abs offer left" style="right:782px;top:2031px">AI-powered<br>Customer Support<span class="ico"><svg width="26" height="26" viewBox="0 0 26 26" fill="none" stroke="#2e6a70" stroke-width="2.2"><path d="M5 15v-3a8 8 0 0116 0v3"/><rect x="3" y="14" width="5" height="7" rx="2" fill="#2e6a70"/><rect x="18" y="14" width="5" height="7" rx="2" fill="#2e6a70"/></svg></span></div>
<div class="abs offer" style="left:774px;top:2031px"><span class="ico"><svg width="26" height="26" viewBox="0 0 26 26" fill="none" stroke="#2e6a70" stroke-width="2.2"><circle cx="13" cy="13" r="4"/><path d="M13 3v4M13 19v4M3 13h4M19 13h4M6 6l3 3M17 17l3 3M6 20l3-3M17 9l3-3"/></svg></span>Knowledge<br>System Integration</div>
<div class="abs offer left" style="right:754px;top:2170px">Customer<br>Feedback Insights<span class="ico"><svg width="26" height="26" viewBox="0 0 26 26" fill="#2e6a70"><rect x="3" y="11" width="5" height="11" rx="1"/><path d="M10 11l4-8c2 0 3 1 3 3l-1 5h5c1.5 0 2.5 1.3 2 3l-2 6c-.4 1.3-1.4 2-2.7 2H10z"/></svg></span></div>
<div class="abs offer" style="left:752px;top:2170px"><span class="ico"><svg width="28" height="26" viewBox="0 0 28 26" fill="#2e6a70"><path d="M2 4h16v11H8l-4 4v-4H2z"/><path d="M12 17h10l4 4V10h-6v7z" opacity=".6"/><circle cx="6" cy="10" r="1.3" fill="#e3f2f2"/><circle cx="10" cy="10" r="1.3" fill="#e3f2f2"/><circle cx="14" cy="10" r="1.3" fill="#e3f2f2"/></svg></span>AI help Desks<br>and Chat Agents</div>
<div class="abs ico" style="left:572px;top:2272px"><svg width="26" height="26" viewBox="0 0 26 26" fill="none" stroke="#2e6a70" stroke-width="2.2"><circle cx="13" cy="13" r="5"/><circle cx="13" cy="13" r="10" stroke-dasharray="4 3"/></svg></div>
<div class="abs" style="left:0;width:1228px;top:2333px;text-align:center;font-size:15px;font-weight:500">Data integration and deployment</div>
<div class="abs ghost">OUR KEY OFFERINGS</div>

<h2 class="abs section-title" style="top:2484px">Latest <span class="swoosh">News</span></h2>

<article class="abs news" style="left:122px"><div class="thumb" role="img" aria-label="Photo of a small robot working at a laptop" style="background:linear-gradient(135deg,#d8d2c8,#8a7360 60%,#4c3c30)"></div><p class="meta">August 20, 2024</p><div class="row"><h5>Lorem ipsum dolor sit amet,<br>consectetur adipiscing elit.</h5><span class="arrow"><svg width="10" height="10" viewBox="0 0 10 10"><path d="M2 5h6M5 2l3 3-3 3" stroke="#fff" stroke-width="1.3" fill="none"/></svg></span></div></article>
<article class="abs news" style="left:447px"><div class="thumb" role="img" aria-label="Photo of hands typing on a laptop with a customer relationship interface overlay" style="background:linear-gradient(135deg,#e4e6e7,#a2a8ab 55%,#5d6366)"></div><p class="meta">August 20, 2024</p><div class="row"><h5>Lorem ipsum dolor sit amet,<br>consectetur adipiscing elit.</h5><span class="arrow"><svg width="10" height="10" viewBox="0 0 10 10"><path d="M2 5h6M5 2l3 3-3 3" stroke="#fff" stroke-width="1.3" fill="none"/></svg></span></div></article>
<article class="abs news" style="left:772px"><div class="thumb" role="img" aria-label="Photo of a woman working at a laptop with holographic charts" style="background:linear-gradient(135deg,#2a2b3a,#6a4a6a 45%,#b48a72)"></div><p class="meta">August 20, 2024</p><div class="row"><h5>Lorem ipsum dolor sit amet,<br>consectetur adipiscing elit.</h5><span class="arrow"><svg width="10" height="10" viewBox="0 0 10 10"><path d="M2 5h6M5 2l3 3-3 3" stroke="#fff" stroke-width="1.3" fill="none"/></svg></span></div></article>

<div class="abs view-all">View All News</div>

<footer>
  <div class="abs foot-line" style="top:2902px"></div>
  <div class="abs vline" style="left:374px"></div>
  <div class="abs vline" style="left:636px"></div>
  <div class="abs vline" style="left:893px"></div>
  <div class="abs" style="left:121px;top:2928px;width:210px">
    <div class="brand" style="font-size:22px"><span class="brand-dot" style="width:34px;height:34px"></span>BriskLoom</div>
    <p style="font-size:9px;line-height:14.5px;margin-top:16px">Lorem ipsum dolor sit amet, consectetur adipiscing elit. Duis venenatis, eros at ultricies consectetur, leo dui condimentum nisl, non tempor libero eros ut nunc.</p>
  </div>
  <div class="abs foot-col" style="left:449px;top:2932px"><h6>Quick Links</h6><ul><li>Product</li><li>Platform</li><li>Company</li><li>News</li><li>Learn More</li></ul></div>
  <div class="abs foot-col" style="left:700px;top:2932px"><h6>Contact Us</h6>
    <div class="contact-row"><i><svg width="11" height="11" viewBox="0 0 12 12"><path d="M3 1l2 2-1 1.5a7 7 0 003.5 3.5L9 7l2 2-1.5 2A9 9 0 011 2.5z" fill="#fff"/></svg></i>555-010-2746</div>
    <div class="contact-row"><i><svg width="11" height="9" viewBox="0 0 12 9"><rect x=".5" y=".5" width="11" height="8" fill="none" stroke="#fff"/><path d="M.5 .5L6 5l5.5-4.5" fill="none" stroke="#fff"/></svg></i>hello@briskloom.example</div>
  </div>
  <div class="abs foot-col" style="left:990px;top:2932px"><h6>Follow Us</h6>
    <div class="social-row"><i></i>Friendwall</div>
    <div class="social-row"><i></i>Workmesh</div>
    <div class="social-row"><i></i>Chirpline</div>
  </div>
  <div class="abs foot-line" style="top:3085px"></div>
  <p class="abs copy">© 2024 by BriskLoom. All Rights Reserved</p>
</footer>

</body>
</html>
```